Criminal Defense Lawyer Business Card

I am starting a new criminal defense law office in New Jersey and I need a business card for potential clients. I plan to use technology to increase the client's connection with their criminal defense. I wish to use the motto: "Connect With Your Defense."
I have a QR code that I would ask you to consider including in the design.
Attached are samples from the current draft card.

The people looking at this card are frightened and seeking someone who can help them with their unexpected arrest.
The final design should communicate sophistication, technological skill, and aggressive representation.
Updates

Reason: Final review of designs. Thank you for the designs.

Target Market(s)

Industry/Entity Type

Defense

Contact Information for Business Card

Everett Lansford
(844) TX Shielded – toll free
(844) 917-4403
(609) 481-7725
(732) 604-1159
(908) 273-6641

Rett@TX Shielded.com
www.TX Shielded.com

“Connect With Your Defense”

Law Office of Everett Lansford, L.L.C.

Former State & Federal Prosecutor – 15 Years Experience
Contact Now for a Free Initial Consultation

Requirements
Must have
• “Connect With Your Defense”
TXShielded.com
Nice to have
• Aggressive Criminal Defense & DUI Defense

QR code is the logo. (Ignore if you feel design is better without the QR code)
Should not have
• May not say "specialist" or "specialize" or claim to be the best. (New Jersey lawyer rules.)
Address is intentionally left off.

```html
<!DOCTYPE html>
<html lang="en">
<head>
<meta charset="utf-8">
<title>Everett Lansford – Business Card</title>
<link rel="stylesheet" href="https://fonts.googleapis.com/css2?family=Arimo:wght@400&family=Open+Sans:wght@400;600&family=Archivo+Narrow:ital,wght@1,500;1,600&display=swap">
<style>
  :root {
    --backdrop: #d9d9db;
    --silver-light: #d2d4d7;
    --silver-mid: #a7a9ad;
    --silver-dark: #7d7f83;
    --band-dark: #3a3b3e;
    --band-mid: #6d6f73;
    --ink: #2b2c2e;
    --ink-soft: #3d3e41;
    --white: #ffffff;
    --emblem-fill: #46474a;
  }
  * { box-sizing: border-box; margin: 0; padding: 0; }
  html, body {
    width: 1200px; height: 914px; overflow: hidden;
    background: var(--backdrop);
  }
  .sheet {
    position: relative; width: 1200px; height: 914px;
    display: flex; gap: 40px; align-items: center; justify-content: center;
  }
  .card {
    position: relative; width: 540px; height: 309px; overflow: hidden;
    background: linear-gradient(125deg, var(--silver-dark) 0%, var(--silver-mid) 30%, var(--silver-light) 55%, var(--silver-mid) 80%, var(--silver-dark) 100%);
    box-shadow: 0 6px 18px rgba(0,0,0,.25);
  }

  /* Front */
  .card-front .rule-dark {
    position: absolute; left: 60px; right: 0; top: 62px; height: 16px;
    background: linear-gradient(90deg, var(--band-dark), var(--band-mid) 50%, var(--band-dark));
  }
  .card-front .motto-band {
    position: absolute; left: 60px; right: 0; top: 78px; height: 34px;
    background: linear-gradient(90deg, var(--silver-mid), var(--silver-light) 60%, var(--silver-mid));
    border-bottom: 6px solid var(--band-dark);
  }
  .motto {
    position: absolute; right: 22px; top: 84px;
    font: 400 15px/1 "Open Sans", sans-serif; color: var(--white); letter-spacing: .2px;
  }
  .emblem { position: absolute; left: 20px; top: 24px; }
  .name {
    position: absolute; left: 24px; top: 148px;
    font: 400 25px/1 "Arimo", sans-serif; color: var(--ink);
  }
  .title {
    position: absolute; left: 24px; top: 184px;
    font: 400 14px/1 "Open Sans", sans-serif; color: var(--ink-soft);
  }
  .contact-list {
    position: absolute; left: 24px; top: 212px; list-style: none;
    font: 400 14px/1 "Open Sans", sans-serif; color: var(--white);
  }
  .contact-list li { display: flex; align-items: center; gap: 8px; height: 26px; }
  .tagline {
    position: absolute; right: 22px; top: 180px;
    font: italic 600 17px/1 "Archivo Narrow", sans-serif; color: var(--white);
  }
  .phones {
    position: absolute; right: 22px; top: 210px; text-align: right;
    font: 400 14px/1.6 "Open Sans", sans-serif; color: var(--ink);
  }
  .phones .pair span + span { margin-left: 18px; }

  /* Back */
  .card-back .watermark {
    position: absolute; left: 170px; top: 50px; width: 200px; height: 200px;
    border-radius: 50%;
    background: radial-gradient(circle, rgba(120,122,126,.35), rgba(120,122,126,0) 70%);
  }
  .card-back .firm {
    position: absolute; left: 0; right: 0; top: 96px; text-align: center;
    font: italic 600 17px/1.45 "Archivo Narrow", sans-serif; color: var(--ink);
  }
  .card-back .cta {
    position: absolute; left: 0; right: 0; top: 232px; text-align: center;
    font: 400 15px/1 "Open Sans", sans-serif; color: var(--ink-soft);
  }
</style>
</head>
<body>
<main class="sheet">
  <section class="card card-back" aria-label="Card back">
    <div class="watermark" role="img" aria-label="Faint scales of justice emblem"></div>
    <p class="firm">Law Office of Everett Lansford, L.L.C. Former State &amp; Federal Prosecutor<br>15 Years Experience</p>
    <p class="cta">Contact Now for a Free Initial Consultation</p>
  </section>

  <section class="card card-front" aria-label="Card front">
    <div class="rule-dark"></div>
    <div class="motto-band"></div>
    <p class="motto">“Connect With Your Defense”</p>

    <svg class="emblem" width="102" height="102" viewBox="0 0 102 102" role="img" aria-label="Scales of justice emblem">
      <circle cx="51" cy="51" r="49" fill="#c9cbce" stroke="#8a8c90" stroke-width="2"/>
      <circle cx="51" cy="51" r="42" fill="var(--emblem-fill)"/>
    </svg>

    <h1 class="name">Everett Lansford</h1>
    <p class="title">Attorney-At-Law</p>
    <ul class="contact-list">
      <li>
        <svg width="16" height="12" viewBox="0 0 16 12" aria-hidden="true"><rect x="0.5" y="0.5" width="15" height="11" fill="#fff" stroke="#555"/><path d="M1 1 L8 7 L15 1" fill="none" stroke="#555" stroke-width="1.2"/></svg>
        Rett@TXShielded.com
      </li>
      <li>
        <svg width="16" height="16" viewBox="0 0 16 16" aria-hidden="true" fill="none" stroke="#444" stroke-width="1.2"><circle cx="8" cy="8" r="7"/><ellipse cx="8" cy="8" rx="3" ry="7"/><path d="M1 8h14M2.5 4.5h11M2.5 11.5h11"/></svg>
        www.TXShielded.com
      </li>
    </ul>

    <p class="tagline">“Aggressive Criminal Defense &amp; DUI Defense”</p>
    <div class="phones">
      <div>(844) TXShielded - Toll Free</div>
      <div class="pair"><span>(844) 917-4403</span><span>(732) 604-1159</span></div>
      <div class="pair"><span>(609) 481-7725</span><span>(908) 273-6641</span></div>
    </div>
  </section>
</main>
</body>
</html>
```